Website for Foodstuff Import-Export Company *

We need a website for our company which imports and sell ( edible oil , ketchup , mayonnaise and pulses ). our current website is brevonix.pl , we need a website which has corporate appearance with good quality products.

Target Market(s)

European Wholesalers , Supermarket Chains,

Coding

Coded - Design and coding required

Number of Pages Required

1 page

```html
<!DOCTYPE html>
<html lang="en">
<head>
<meta charset="utf-8">
<title>Brevonix – Foodstuff Import &amp; Export</title>
<link rel="stylesheet" href="https://fonts.googleapis.com/css2?family=Montserrat:wght@400;500;600;700;800;900&display=swap">
<style>
:root{
  --green:#7cb83a;
  --green-dark:#1f9a4a;
  --teal:#1aa57e;
  --orange:#f36d21;
  --orange-light:#f7923a;
  --amber:#f3b32b;
  --text:#555;
  --heading:#222;
  --grey-bg:#eeeeee;
  --footer:#0f3a22;
  --white:#fff;
}
*{margin:0;padding:0;box-sizing:border-box}
html,body{width:1200px;height:3400px;overflow:hidden}
body{position:relative;font-family:'Montserrat',sans-serif;color:var(--text);background:var(--white)}
.abs{position:absolute}

/* header */
.topline{left:0;top:0;width:1200px;height:3px;background:var(--green)}
.header{left:0;top:3px;width:1200px;height:102px;background:var(--white);z-index:3}
.logo{left:143px;top:20px;width:200px;height:152px;border-radius:0 0 100px 100px;background:var(--white);z-index:5;display:flex;flex-direction:column;align-items:center;justify-content:center;gap:10px;padding-top:10px}
.logo-dot{width:46px;height:46px;border-radius:50%;background:var(--green)}
.logo-name{font-size:27px;font-weight:600;color:var(--teal);letter-spacing:1px}
.phone{left:745px;top:10px;height:36px;display:flex;align-items:center;gap:10px;font-size:21px;font-weight:800;color:var(--heading);z-index:4}
.phone .lbl{color:var(--green)}
.nav{left:430px;top:62px;width:770px;height:43px;background:var(--green);clip-path:polygon(35px 0,100% 0,100% 100%,0 100%);display:flex;align-items:center;z-index:4}
.nav a{color:var(--white);text-decoration:none;font-size:15px;font-weight:500;padding:0 16px;height:43px;line-height:43px}
.nav a.active{background:var(--amber);margin-left:0;padding-left:38px;padding-right:18px;clip-path:polygon(35px 0,100% 0,100% 100%,0 100%);margin-left:0}
.nav a.active{background:var(--amber)}
.search{margin-left:22px;width:134px;height:24px;background:var(--white);display:flex;align-items:center;justify-content:space-between;padding:0 8px;font-size:10px;font-style:italic;color:#999}

/* hero */
.hero-img{left:0;top:105px;width:1200px;height:620px;background:
 radial-gradient(ellipse 380px 200px at 600px 480px,#c8402a 0%,#e4a23a 40%,rgba(0,0,0,0) 75%),
 radial-gradient(ellipse 420px 260px at 200px 300px,#d9a21e 0%,#9c7012 50%,rgba(0,0,0,0) 80%),
 linear-gradient(180deg,#2c5a1d 0%,#5e8a3a 45%,#c9d2c1 75%,#e8ebe6 100%)}
.hero-curve{left:0;top:560px;width:1200px;height:180px;z-index:2}
.hero-title{left:695px;top:198px;font-size:45px;line-height:51px;font-weight:900;color:var(--white);z-index:2}
.btn{display:inline-flex;align-items:center;justify-content:center;border-radius:30px;background:linear-gradient(180deg,var(--orange-light),var(--orange));color:var(--white);font-weight:700;text-transform:uppercase}
.hero-btn{left:695px;top:432px;width:150px;height:48px;font-size:14px;z-index:2}
.dots{left:1125px;top:280px;display:flex;flex-direction:column;gap:10px;z-index:2}
.dots span{width:8px;height:8px;border-radius:50%;background:var(--white)}
.dots span.on{background:none;border:2px solid var(--white)}

/* section heading */
.section-title{font-size:45px;font-weight:600;background:linear-gradient(90deg,var(--teal),var(--green));-webkit-background-clip:text;background-clip:text;color:transparent}

/* about */
.about-title{left:145px;top:808px}
.about-text{left:145px;top:878px;width:430px;font-size:12.5px;line-height:24px;color:#666}
.about-btn{left:145px;top:1118px;width:120px;height:38px;font-size:11px}
.about-frame{left:614px;top:780px;width:466px;height:402px;border:6px solid var(--green-dark);border-left:none;border-top:none}
.about-frame:before{content:"";position:absolute;right:-6px;top:0;width:6px;height:10px}
.about-img{left:614px;top:780px;width:442px;height:378px;background:
 radial-gradient(ellipse 100px 70px at 130px 200px,#f3dc8a,#e8c566 60%,rgba(0,0,0,0) 100%),
 radial-gradient(ellipse 140px 160px at 340px 140px,#f3b43e,#e59527 50%,rgba(0,0,0,0) 100%),
 linear-gradient(160deg,#5a3a24,#3c2a20 55%,#2a2a2a)}
.about-bar{left:1074px;top:780px;width:6px;height:402px;background:var(--green-dark)}

/* products */
.products-bg{left:0;top:1277px;width:1200px;height:608px;background:var(--grey-bg)}
.products-title{left:0;top:1370px;width:1200px;text-align:center}
.card{width:440px;height:170px;background:var(--white);border-radius:85px;box-shadow:0 4px 12px rgba(0,0,0,.08)}
.card .thumb{position:absolute;left:15px;top:18px;width:134px;height:134px;border-radius:50%}
.card h3{position:absolute;left:170px;top:26px;font-size:17px;font-weight:500;color:var(--heading)}
.card p{position:absolute;left:170px;top:60px;width:250px;font-size:11.5px;line-height:20px;color:#777}
.card .more{position:absolute;left:170px;top:130px;font-size:11.5px;font-weight:700;color:var(--green)}
.c1{left:152px;top:1494px}.c2{left:610px;top:1494px}.c3{left:152px;top:1694px}.c4{left:610px;top:1694px}
.t-oil{background:radial-gradient(circle,#f2d27a,#e2e2dc 70%)}
.t-ket{background:radial-gradient(circle,#c43a22,#e9c96a 60%,#d8d6cc)}
.t-mayo{background:radial-gradient(circle,#faf5e6 40%,#8a5a3a)}
.t-pulse{background:radial-gradient(circle,#c89a4a,#8a3a22 60%,#5a3a2a)}
.centre-mark{left:588px;top:1666px;width:24px;height:24px;border-radius:50%;background:var(--green)}
.oil-band{left:0;top:1884px;width:1200px;height:398px;background:linear-gradient(180deg,#ececec 0%,#f1d35a 45%,#e9be1a 62%,#e6c21c 100%)}

/* contact */
.contact-title{left:0;top:2372px;width:1200px;text-align:center}
.office{width:300px}
.office .pin{width:60px;height:60px;border-radius:50%;background:var(--green);display:flex;align-items:center;justify-content:center}
.office .pin.dark{background:var(--green-dark)}
.office h4{margin-top:22px;font-size:19px;font-weight:700;color:var(--heading)}
.office p{margin-top:10px;font-size:13.5px;line-height:22px;color:#666}
.o1{left:165px;top:2497px}.o2{left:488px;top:2497px}.o3{left:790px;top:2497px}
.field{border:1px solid #ccc;font-size:12px;color:#666;padding:25px 22px}
.f1{left:233px;top:2743px;width:362px;height:55px;padding-top:20px}
.f2{left:604px;top:2743px;width:362px;height:55px;padding-top:20px}
.f3{left:233px;top:2808px;width:362px;height:55px;padding-top:20px}
.f4{left:604px;top:2808px;width:362px;height:55px;padding-top:20px}
.f5{left:233px;top:2873px;width:733px;height:118px;padding-top:20px}
.submit{left:516px;top:3016px;width:168px;height:39px;font-size:11px}

/* footer */
.footer{left:0;top:3130px;width:1200px;height:270px}
.social{left:506px;top:3230px;display:flex;gap:9px}
.social span{width:41px;height:41px;border-radius:50%;border:2px solid var(--white)}
.footer-nav{left:0;top:3300px;width:1200px;text-align:center;font-size:22px;font-weight:700;color:var(--white);word-spacing:4px}
.footer-nav i{font-style:normal;margin:0 14px}
.copyright{left:0;top:3355px;width:1200px;text-align:center;font-size:11.5px;color:var(--white)}
</style>
</head>
<body>

<div class="abs topline"></div>
<div class="abs header"></div>
<div class="abs logo"><span class="logo-dot"></span><span class="logo-name">BREVONIX</span></div>
<div class="abs phone">
  <svg width="34" height="34" viewBox="0 0 34 34"><circle cx="17" cy="17" r="15" fill="none" stroke="#7cb83a" stroke-width="2"/><path d="M11 9c1-1 2-1 3 0l2 3c.5 1 0 2-1 2.5 1 2.5 3 4.5 5.5 5.5.5-1 1.5-1.5 2.5-1l3 2c1 1 1 2 0 3-2 2-5 2-8 0-3-2-6-5-8-8-2-3-1-5 1-7z" fill="#7cb83a"/></svg>
  <span><span class="lbl">Phone :</span> +4917655501234</span>
</div>
<nav class="abs nav">
  <a class="active">HOME</a><a>ABOUT US</a><a>PRODUCTS</a><a>CONTACT US</a>
  <div class="search"><span>Search</span><svg width="10" height="10" viewBox="0 0 10 10"><circle cx="4" cy="4" r="3" fill="none" stroke="#333" stroke-width="1.5"/><path d="M6.3 6.3L9 9" stroke="#333" stroke-width="1.5"/></svg></div>
</nav>

<div class="abs hero-img" role="img" aria-label="Hand pouring olive oil from a bottle onto a fresh salad with tomatoes, peppers and olives"></div>
<svg class="abs hero-curve" viewBox="0 0 1200 180" aria-hidden="true">
  <path d="M0,105 C250,45 450,55 650,135 C850,200 1050,150 1200,100 L1200,180 L0,180 Z" fill="#fff"/>
  <path d="M0,105 C250,45 450,55 650,135 C850,200 1050,150 1200,100" fill="none" stroke="#1f9a4a" stroke-width="6"/>
</svg>
<h1 class="abs hero-title">BEST NATURAL<br>NUTRITIONAL<br>SOURCES OF<br>VITAMIN E</h1>
<div class="abs btn hero-btn">Get Started</div>
<div class="abs dots"><span></span><span></span><span class="on"></span><span></span><span></span></div>

<h2 class="abs section-title about-title">ABOUT US</h2>
<p class="abs about-text">BREVONIX is a manufacturing and trading company in Wrocław , Poland We established longer and closer working relationships with our clients and supplier not only provide immediate and reliable service but to continually exceed expectations and goals. We create commercial flows, import and export products, arranging and managing international projects with our partners.Supported our network, we are able to integrate all these functions with our fruitful experience. Our numerous competencies allow us to respond to the needs of industries looking for a new market.</p>
<div class="abs btn about-btn">Read More</div>
<div class="abs about-frame"></div>
<div class="abs about-bar"></div>
<div class="abs about-img" role="img" aria-label="French fries with ketchup and mayonnaise dips on a wooden table"></div>

<div class="abs products-bg"></div>
<h2 class="abs section-title products-title">OUR PRODUCTS</h2>
<div class="abs card c1"><div class="thumb t-oil" role="img" aria-label="Bottles of edible oil"></div><h3>OILS &amp; FATS</h3><p>Lorem ipsum dolor sit amsectedipiscing elit, sed do eiusmod tempor incididunt ut labore et dolore magna aliqua.</p><span class="more">READ MORE</span></div>
<div class="abs card c2"><div class="thumb t-ket" role="img" aria-label="Bowls of ketchup and sauces"></div><h3>KETCHUP &amp; SAUCES</h3><p>Lorem ipsum dolor sit amsectedipiscing elit, sed do eiusmod tempor incididunt ut labore et dolore magna aliqua.</p><span class="more">READ MORE</span></div>
<div class="abs card c3"><div class="thumb t-mayo" role="img" aria-label="Bowl of mayonnaise with parsley"></div><h3>MAYONNAISE</h3><p>Lorem ipsum dolor sit amsectedipiscing elit, sed do eiusmod tempor incididunt ut labore et dolore magna aliqua.</p><span class="more">READ MORE</span></div>
<div class="abs card c4"><div class="thumb t-pulse" role="img" aria-label="Bowls of assorted pulses and beans"></div><h3>PULSES</h3><p>Lorem ipsum dolor sit amsectedipiscing elit, sed do eiusmod tempor incididunt ut labore et dolore magna aliqua.</p><span class="more">READ MORE</span></div>
<div class="abs centre-mark"></div>
<div class="abs oil-band" role="img" aria-label="Row of edible oil bottles above a pool of golden oil, with oil pouring from a glass"></div>

<h2 class="abs section-title contact-title">CONTACT US</h2>
<div class="abs office o1"><div class="pin"><svg width="18" height="24" viewBox="0 0 18 24"><path d="M9 0C4 0 0 4 0 9c0 6 9 15 9 15s9-9 9-15c0-5-4-9-9-9z" fill="#fff"/><circle cx="9" cy="9" r="3.5" fill="#7cb83a"/></svg></div><h4>OFFICE</h4><p>Ul. Ogrodowa 12 /8a<br>50-101 Wrocław Polska<br>Phone : +48712345670</p></div>
<div class="abs office o2"><div class="pin dark"><svg width="18" height="24" viewBox="0 0 18 24"><path d="M9 0C4 0 0 4 0 9c0 6 9 15 9 15s9-9 9-15c0-5-4-9-9-9z" fill="#fff"/><circle cx="9" cy="9" r="3.5" fill="#1f9a4a"/></svg></div><h4>WAREHOUSE POLAND</h4><p>Polna 18, 55-300 Środa<br>Śląska ,Poland</p></div>
<div class="abs office o3"><div class="pin"><svg width="18" height="24" viewBox="0 0 18 24"><path d="M9 0C4 0 0 4 0 9c0 6 9 15 9 15s9-9 9-15c0-5-4-9-9-9z" fill="#fff"/><circle cx="9" cy="9" r="3.5" fill="#7cb83a"/></svg></div><h4>WAREHOUSE &nbsp;GERMANY</h4><p>Lindenweg 9, 50126<br>Bergheim, Germany<br>Phone : +4917655501234<br>info@brevonix.pl</p></div>

<div class="abs field f1">First Name</div>
<div class="abs field f2">Last Name</div>
<div class="abs field f3">Email address</div>
<div class="abs field f4">Phone Number</div>
<div class="abs field f5">Message</div>
<div class="abs btn submit">Submit Message</div>

<svg class="abs footer" viewBox="0 0 1200 270" aria-hidden="true">
  <defs><linearGradient id="fg" x1="0" y1="0" x2="0" y2="1"><stop offset="0" stop-color="#164a2b"/><stop offset="1" stop-color="#0c2f1b"/></linearGradient></defs>
  <path d="M0,40 C300,-10 500,70 700,90 C900,110 1050,70 1200,40 L1200,270 L0,270 Z" fill="url(#fg)"/>
  <path d="M0,40 C300,-10 500,70 700,90 C900,110 1050,70 1200,40" fill="none" stroke="#7cb83a" stroke-width="5"/>
</svg>
<div class="abs social"><span></span><span></span><span></span><span></span></div>
<div class="abs footer-nav">HOME<i>/</i>ABOUT US<i>/</i>PRODUCTS<i>/</i>CONTACT US</div>
<div class="abs copyright">Copyright © 2020 Brevonix. All rights reserved &nbsp;| &nbsp;Terms of use &nbsp;| &nbsp;Privacy policy</div>

</body>
</html>
```